website design for Company MVR

Our company name MVR(the grand mural limited), need design a website. It is a website that focuses on promoting art design in the world.
We will provide the existing logo design, the new website and logo should be matched to each other. The website has to include pages "Home" "Contact" "Service" and So on at least 6-8 pages. The site is mainly for publicity and promotion. We will have an existing domain and hosting.
Updates

We prefer the original design, thanks.

Target Market(s)

large public art

Industry/Entity Type

Architecture and design, large public art and sculpture manufacturer

Coding

Coded - Design and coding required

Number of Pages Required

5+ page

Requirements
Must have
• 1. the overall color has to match our logo color 2. Do not need to do any change on our logo including the color 3. Here is a similar style of the home page we like, it can be similar but must not same. Pls check the below link. https://www.velmardo.it/en-us/

```html
<!DOCTYPE html>
<html lang="en">
<head>
<meta charset="utf-8">
<title>MVR — The Grand Mural</title>
<link href="https://fonts.googleapis.com/css2?family=Jost:wght@300;400;500;600;700&display=swap" rel="stylesheet">
<style>
:root{
  --ink:#1c1c1c;
  --muted:#555;
  --line:#9a9a9a;
  --gold-1:#a9904a;
  --gold-2:#d9c98e;
  --gold-3:#efe6c6;
  --soft:#f5f1ef;
  --pale:#f7f7f7;
  --accent:#35a7e0;
  --footer-a:#9aa1a6;
  --footer-b:#2e5a6d;
  --footer-c:#14445c;
  --footer-bar:#0e3a52;
  --white:#ffffff;
}
*{box-sizing:border-box;margin:0;padding:0}
html,body{width:1200px;height:4766px;overflow:hidden}
body{position:relative;background:var(--white);font-family:"Jost",Arial,sans-serif;color:var(--ink)}
.abs{position:absolute}
.site-header{left:0;top:0;width:1200px;height:41px;background:var(--white)}
.brand{left:32px;top:8px;display:flex;align-items:center;gap:8px;font-size:22px;font-weight:600;letter-spacing:1px}
.brand small{font-size:10px;font-weight:400;letter-spacing:1.5px;line-height:1.05;color:var(--muted)}
.burger{right:32px;top:13px;width:22px}
.burger span{display:block;height:2px;background:var(--ink);margin-bottom:4px}
.hero{left:0;top:41px;width:1200px;height:588px;background:
  linear-gradient(160deg,rgba(255,255,255,0) 55%,rgba(248,240,212,.7) 56%,rgba(248,240,212,.2) 100%),
  radial-gradient(ellipse at 48% 88%,#8f7347 0%,rgba(143,115,71,0) 35%),
  linear-gradient(135deg,#9b8240 0%,#c9b26c 40%,#e6d9a8 65%,#c7b47a 100%);color:var(--white)}
.hero-kicker{left:186px;font-size:11px}
.hero-title{left:186px;font-size:32px;font-weight:400;letter-spacing:.5px}
.hero-text{left:186px;width:420px;font-size:11px;line-height:1.6}
.hero-btn{left:194px;width:118px;height:34px;background:var(--white);color:var(--muted);font-size:12px;display:flex;align-items:center;justify-content:center;border-radius:2px}
.follow{left:1010px;top:140px;width:30px;height:240px;display:flex;flex-direction:column;align-items:center;gap:16px}
.follow i{display:block;width:8px;height:8px;background:var(--white);border-radius:2px}
.follow span{writing-mode:vertical-rl;transform:rotate(180deg);font-size:10px;margin-top:20px}
.feature{top:505px;display:flex;gap:18px;font-size:11px;line-height:1.7;align-items:flex-start}
.feature svg{margin-top:4px}
.hero-divider{left:1028px;width:1px;height:110px;background:rgba(255,255,255,.6)}
.to-top{left:1098px;width:40px;height:40px;border:1.5px solid var(--white);border-radius:50%}
.section-title{width:1200px;left:0;text-align:center;font-weight:600}
.about-text{left:22px;top:718px;width:1156px;text-align:center;font-size:11.5px;line-height:1.65;color:#333}
.photo{position:absolute}
.events-line{left:600px;width:1.5px;background:var(--line)}
.event-date{left:0;width:1200px;text-align:center;font-size:12px;line-height:16px}
.event-dot{left:594px;width:14px;height:14px;border:1.5px solid var(--line);border-radius:50%;background:var(--white)}
.event-title{left:632px;font-size:20px;font-weight:500}
.event-text{left:632px;width:380px;font-size:11px;line-height:1.75;color:#333}
.partner{top:3162px;width:52px;height:44px;background:#d6d6d6;border-radius:4px}
.partner.round{border-radius:50%;width:48px;height:48px;top:3160px}
.updates-band{left:0;top:3384px;width:1200px;height:181px;background:var(--soft)}
.updates-text{left:310px;top:3396px;width:580px;text-align:center;font-size:11.5px;line-height:1.7;color:#333}
.field{height:30px;background:var(--white);border:1px solid #e5e1de;font-size:10px;color:#999;padding:0 12px;display:flex;align-items:center}
.btn-sub{left:802px;top:3469px;width:82px;height:30px;background:var(--accent);color:var(--white);font-size:11px;font-weight:600;display:flex;align-items:center;justify-content:center}
.contact-title{left:242px;top:3636px;font-size:31px;font-weight:600}
.contact-lead{left:242px;top:3694px;width:200px;font-size:11px;line-height:1.7}
.submit{left:242px;top:3845px;width:200px;height:30px;background:var(--white);border:1px solid #eee;font-size:11px;display:flex;align-items:center;justify-content:center;box-shadow:0 1px 2px rgba(0,0,0,.08)}
.map-band{left:0;top:3972px;width:1200px;height:438px;background:var(--pale)}
.map-area{left:0;top:4080px;width:1200px;height:330px;background:linear-gradient(135deg,#eef0ea 0%,#e3e8df 40%,#dde4ea 70%,#eceeee 100%)}
.site-footer{left:0;top:4410px;width:1200px;height:296px;background:linear-gradient(100deg,var(--footer-a) 0%,#6f8791 35%,var(--footer-b) 70%,var(--footer-c) 100%);color:var(--white)}
.f-col{top:30px;font-size:11px;line-height:1.75}
.f-col h4{font-size:12px;font-weight:600;margin-bottom:28px}
.socials{display:flex;gap:8px;margin-top:14px;margin-left:22px}
.socials i{width:20px;height:20px;border-radius:50%;background:var(--white);display:block}
.f-input{left:832px;width:200px;height:30px;background:var(--white);border-radius:8px;color:#aaa;font-size:9px;padding:8px 10px}
.f-send{left:840px;width:118px;height:30px;background:var(--white);color:var(--ink);font-size:11px;display:flex;align-items:center;justify-content:center;letter-spacing:.5px}
.footer-bar{left:0;top:4706px;width:1200px;height:60px;background:var(--footer-bar);color:#dce6ec;font-size:11px;display:flex;align-items:center;justify-content:center}
</style>
</head>
<body>

<header class="abs site-header">
  <div class="abs brand">MVR <small>THE<br>GRAND MURAL</small></div>
  <div class="abs burger"><span></span><span></span><span></span></div>
</header>

<section class="abs hero" role="img" aria-label="Gallery interior with a large sculpture of a horned animal under a slanted ceiling">
  <p class="abs hero-kicker" style="top:156px">We are here for</p>
  <h1 class="abs hero-title" style="top:176px">TO SHOW YOU THE ART</h1>
  <p class="abs hero-text" style="top:225px">Loans are advantageous as a relatively inexpensive way of borrowing money. We believe in those made to do more.</p>
  <div class="abs hero-btn" style="top:296px">View more</div>
  <div class="abs follow"><i></i><i></i><i></i><i></i><span>Follow us</span></div>
  <div class="abs feature" style="left:186px">
    <svg width="20" height="18" viewBox="0 0 20 18" fill="none" stroke="#fff" stroke-width="1.2"><rect x="1" y="2" width="18" height="15"/><line x1="1" y1="6" x2="19" y2="6"/><line x1="6" y1="9" x2="6" y2="15"/><line x1="10" y1="9" x2="10" y2="15"/><line x1="14" y1="9" x2="14" y2="15"/></svg>
    <div>Quick<br>Loan approvals</div>
  </div>
  <div class="abs feature" style="left:470px">
    <svg width="20" height="20" viewBox="0 0 20 20" fill="none" stroke="#fff" stroke-width="1.2"><circle cx="10" cy="10" r="8.5"/><path d="M6 12a4.5 4.5 0 0 0 8 0"/></svg>
    <div>20,000<br>Customers satisfaction</div>
  </div>
  <div class="abs feature" style="left:752px">
    <svg width="20" height="20" viewBox="0 0 20 20" fill="none" stroke="#fff" stroke-width="1.2"><path d="M10 2 2 6l8 4 8-4z"/><path d="M2 10l8 4 8-4"/><path d="M2 14l8 4 8-4"/></svg>
    <div>No prepayment or<br>hidden fees</div>
  </div>
  <div class="abs hero-divider" style="top:439px"></div>
  <div class="abs to-top" style="top:496px"><svg width="37" height="37" viewBox="0 0 37 37"><path d="M13 21l5.5-5.5L24 21" fill="none" stroke="#fff" stroke-width="1.5"/></svg></div>
</section>

<h2 class="abs section-title" style="top:658px;font-size:30px">About Us</h2>
<p class="abs about-text">Lorem ipsum dolor sit amet, consectetur adipiscing elit. Vivamus a venenatis leo. Integer at luctus elit. Aliquam non placerat nunc, blandit blandit elit. Fusce rhoncus tortor tellus, dignissim molestie risus porttitor vitae. Aenean nec eros neque. Nam dui lectus, vestibulum id eros eget, scelerisque vulputate est. Ut commodo erat leo, eu dignissim elit mattis et. Etiam ultricies facilisis arcu, ut varius nibh pulvinar ac. Integer dignissim nisl a molestie ultrices. Phasellus eget maximus justo, at tristique magna.<br>Quisque eget tellus mi. Aliquam erat volutpat. Quisque a semper risus, ac malesuada nisi. Phasellus interdum eros id odio euismod bibendum. Nam lobortis orci id nisl suscipit, eu dignissim purus tincidunt. Quisque augue lacus, suscipit id dignissim at, tempus eget elit. Suspendisse maximus tempus ante, pellentesque eleifend turpis pulvinar eget. Sed eu sodales tortor, fringilla tempor justo. Quisque suscipit hendrerit augue vehicula luctus. Lorem ipsum dolor sit amet, consectetur adipiscing elit. Interdum et malesuada fames ac ante ipsum primis in faucibus. Nulla urna orci, finibus nec nulla non, dignissim accumsan est.</p>

<div class="photo" style="left:22px;top:897px;width:578px;height:384px;background:radial-gradient(ellipse at 60% 65%,#e9c23a 0%,rgba(233,194,58,0) 45%),linear-gradient(180deg,#dfe4e2 0%,#c9d2cf 35%,#d9b45a 60%,#a97a3c 100%)" role="img" aria-label="Colourful painted canvases on wooden easels"></div>
<div class="photo" style="left:600px;top:897px;width:578px;height:384px;background:radial-gradient(ellipse at 50% 50%,#5c6a52 0%,rgba(92,106,82,0) 45%),linear-gradient(180deg,#2b3630 0%,#3e4c44 55%,#4a4540 80%,#242220 100%)" role="img" aria-label="Dark gallery room with framed classical paintings"></div>
<div class="photo" style="left:22px;top:1281px;width:578px;height:413px;background:linear-gradient(125deg,#2fb0d9 0%,#f3d21c 22%,#f08a1f 40%,#e5304a 58%,#8a3fc4 74%,#2a8fe0 100%)" role="img" aria-label="Close-up of thick colourful paint strokes"></div>
<div class="photo" style="left:600px;top:1281px;width:578px;height:413px;background:radial-gradient(ellipse at 55% 70%,#e6e1d9 0%,rgba(230,225,217,0) 40%),linear-gradient(180deg,#c2ad86 0%,#9a3a2c 35%,#a8382d 55%,#b9b2a8 80%,#7e7b77 100%)" role="img" aria-label="Ornate hall with red walls and white marble statues"></div>

<h2 class="abs section-title" style="top:1754px;font-size:30px">EVENTS</h2>

<div class="abs events-line" style="top:1875px;height:387px"></div>
<div class="abs events-line" style="top:2316px;height:356px"></div>
<div class="abs events-line" style="top:2723px;height:355px"></div>

<p class="abs event-date" style="top:1836px">23 April 2025</p>
<div class="abs event-dot" style="top:1861px"></div>
<div class="photo" style="left:190px;top:1910px;width:378px;height:290px;background:linear-gradient(180deg,#eeeeec 0%,#8a8a8a 25%,#b5b5b5 50%,#7e7e7e 70%,#dcdcda 80%,#c9c9c7 100%)" role="img" aria-label="Gallery wall with black and white panels and a bench"></div>
<h3 class="abs event-title" style="top:1910px">Exhibition 2022</h3>
<p class="abs event-text" style="top:1950px">Lorem ipsum dolor sit amet, consectetur adipiscing elit. Fusce in quam at quam porta lobortis non vitae elit. Fusce sed augue eget orci fermentum malesuada. In auctor leo sed libero semper imperdiet. Integer consequat ultrices lectus, at vestibulum mauris dignissim id. Donec eget dui metus. Quisque suscipit, justo nec tincidunt rhoncus, lorem ligula auctor enim, quis blandit sem sapien vel massa. Morbi placerat ipsum sed est hendrerit sodales..</p>

<p class="abs event-date" style="top:2280px">23 April 2025</p>
<div class="abs event-dot" style="top:2302px"></div>
<div class="photo" style="left:190px;top:2350px;width:378px;height:259px;background:radial-gradient(ellipse at 30% 40%,#6f6a64 0%,rgba(111,106,100,0) 35%),radial-gradient(ellipse at 75% 50%,#8d857c 0%,rgba(141,133,124,0) 40%),linear-gradient(180deg,#efeeec 0%,#e3e0dc 70%,#cfc9c2 100%)" role="img" aria-label="Visitor viewing a large metal wire installation"></div>
<h3 class="abs event-title" style="top:2352px">Exhibition: Metal Art</h3>
<p class="abs event-text" style="top:2391px">Lorem ipsum dolor sit amet, consectetur adipiscing elit. Fusce in quam at quam porta lobortis non vitae elit. Fusce sed augue eget orci fermentum malesuada. In auctor leo sed libero semper imperdiet. Integer consequat ultrices lectus, at vestibulum mauris dignissim id. Donec eget dui metus. Quisque suscipit, justo nec tincidunt rhoncus, lorem ligula auctor enim, quis blandit sem sapien vel massa. Morbi placerat ipsum sed est hendrerit sodales.</p>

<p class="abs event-date" style="top:2686px">23 April 2025</p>
<div class="abs event-dot" style="top:2709px"></div>
<div class="photo" style="left:190px;top:2757px;width:378px;height:251px;background:radial-gradient(ellipse at 45% 60%,#5e6c80 0%,rgba(94,108,128,0) 30%),linear-gradient(90deg,#d6d3cf 0%,#f3f3f1 20%,#ebe9e6 60%,#d2cec8 100%)" role="img" aria-label="Visitors in a white modern art gallery"></div>
<h3 class="abs event-title" style="top:2758px">Exhibition: Modern Art</h3>
<p class="abs event-text" style="top:2797px">Lorem ipsum dolor sit amet, consectetur adipiscing elit. Fusce in quam at quam porta lobortis non vitae elit. Fusce sed augue eget orci fermentum malesuada. In auctor leo sed libero semper imperdiet. Integer consequat ultrices lectus, at vestibulum mauris dignissim id. Donec eget dui metus. Quisque suscipit, justo nec tincidunt rhoncus, lorem ligula auctor enim, quis blandit sem sapien vel massa. Morbi placerat ipsum sed est hendrerit sodales.</p>

<div class="abs partner" style="left:186px"></div>
<div class="abs partner round" style="left:299px"></div>
<div class="abs partner" style="left:408px"></div>
<div class="abs partner" style="left:518px"></div>
<div class="abs partner round" style="left:631px"></div>
<div class="abs partner" style="left:740px"></div>
<div class="abs partner" style="left:850px"></div>
<div class="abs partner" style="left:958px"></div>

<h2 class="abs section-title" style="top:3334px;font-size:31px">Get Latest Updates!</h2>
<div class="abs updates-band"></div>
<p class="abs updates-text">Start with creating a new website and picking up the theme. Then expand the blocks panel with the big red "plus" button in the lower right corner and start dragging the blocks you like.</p>
<div class="abs field" style="left:316px;top:3469px;width:231px">Name</div>
<div class="abs field" style="left:564px;top:3469px;width:226px">Email</div>
<div class="abs btn-sub">Subscribe</div>
<div class="photo" style="left:880px;top:3386px;width:140px;height:179px;background:radial-gradient(ellipse at 55% 12%,#5b86c4 0%,rgba(91,134,196,0) 18%),linear-gradient(180deg,#f1efed,#e4e0dc)" role="img" aria-label="Figure of a person in a white shirt with a blue cap"></div>
<div class="photo" style="left:1130px;top:3530px;width:50px;height:35px;border-radius:50% 50% 0 0;background:linear-gradient(135deg,#8fc2e8,#5ea4d8)" role="img" aria-label="Blue paint splash accent"></div>

<h2 class="abs contact-title">Contact Us</h2>
<p class="abs contact-lead">Fill this form and we'll get back to you soon.</p>
<div class="abs field" style="left:242px;top:3757px;width:200px">Name</div>
<div class="abs field" style="left:242px;top:3800px;width:200px">Email</div>
<div class="abs submit">Submit</div>
<div class="photo" style="left:538px;top:3600px;width:494px;height:329px;background:radial-gradient(circle at 55% 45%,#f6f6f6 0%,#d4d4d4 25%,#9c9c9c 50%,#4a4a4a 80%,#2c2c2c 100%)" role="img" aria-label="Glass dome ceiling seen from below"></div>

<div class="abs map-band"></div>
<h2 class="abs section-title" style="top:3980px;font-size:30px">Map</h2>
<p class="abs section-title" style="top:4026px;font-size:20px;font-weight:400">Find us here</p>
<div class="abs map-area" role="img" aria-label="Street map showing the studio location"></div>

<footer class="abs site-footer">
  <div class="abs f-col" style="left:168px;width:200px">
    <h4>Your Brand Name</h4>
    <p>Vivamus tellus mi. Nulla ne cursus elit,vulputate. Sed ne cursus augue hasellus lacinia sapien vitae.</p>
    <div class="socials"><i></i><i></i><i></i><i></i><i></i></div>
  </div>
  <div class="abs f-col" style="left:390px"><h4>Useful Links</h4><p>Menu 1<br>Menu 2<br>Menu 3<br>Menu 4</p></div>
  <div class="abs f-col" style="left:612px"><h4>Additional Pages</h4><p>Menu 1<br>Menu 2<br>Menu 3</p></div>
  <div class="abs f-col" style="left:832px"><h4>Contact Us</h4></div>
  <div class="abs f-input" style="top:75px">Full Name</div>
  <div class="abs f-input" style="top:116px">E-Mail Address</div>
  <div class="abs f-input" style="top:157px;height:80px">Your Message</div>
  <div class="abs f-send" style="top:248px">SEND MESSAGE</div>
</footer>
<div class="abs footer-bar">Copyright © 2025 MVR. All Rights Reserved.</div>

</body>
</html>
```